Meal Plan Website Needs New Pages Designed

Harvest Table Menus is an online, membership based program that delivers weekly meal programs (7 days worth of recipes plus shopping lists) carefully crafted by an expert team of meal planners. All recipes are created to comply with the following macronutrient ratio: 65% healthy fats, 25% lean protein, 10% good carbs.
All recipes are Paleo friendly and a great resource for those individuals who want to correctly implement this type of diet.

We are re-designing our website and need the following pages designed:

· Home page w/ logo
· How it works page
· Get Started! page
· Recipes Page template (these will be the pages on our site that will have recipes)
· Kitchen Essentials Training page (this will be a page with videos and tips + tricks, PDFs, etc)

So 5 total PSDs, 1 for each page.

Target audience: Men and women between the ages of 30 and 60 who want to:
· Eat healthy
· Lose weight
· Follow/Implement the Paleo diet
· Take the guesswork out of preparing delicious AND healthy meals for them and their families
· Know exactly what to eat, what to buy, how to make it

Feelings/Messages we want to communicate through the design:
· “Organic” but elegant look
· Fresh/light/Airy
· Simple but NOT GENERIC
· “I want to get cooking” feeling

Our Stylistic preferences:
· Minimalist with a few bold elements (something in between)
· Easy to visually navigate (enough white space, but not too much)
· There is more to “see” than to “read”

Our Color Preferences:
· Lighter pallet
· Colors that evoke natural woods, granite countertops…
· Stay away from using all dark colors

Our Font Type Preferences:
· Easy to read
· Not more than 3 font types
· Not too rigid
· Not too sophisticated
· Simple with a touch

Examples of Website Designs that we like:
· http://www.brightbasket41.example/menu-kits/
· http://stonehearth.example/
· https://www.wildforage.example/

```html
<!DOCTYPE html>
<html lang="en">
<head>
<meta charset="utf-8">
<title>Harvest Table Menus – Home</title>
<link rel="stylesheet" href="https://fonts.googleapis.com/css2?family=Open+Sans:wght@400;600&family=Arimo:wght@400&family=Dancing+Script:wght@600&display=swap">
<style>
  :root {
    --teal: #3d5a52;
    --brown: #6b3a12;
    --brown-btn: #5a3416;
    --wood-light: #c68a52;
    --wood-dark: #a8693a;
    --ink: #333;
    --grey-text: #6f6f6f;
    --cream: #f6f5ec;
    --line: #d8d8d8;
    --white: #fff;
  }
  * { margin: 0; padding: 0; box-sizing: border-box; }
  html, body { width: 1200px; height: 2314px; overflow: hidden; background: var(--white); }
  body { position: relative; font-family: "Open Sans", sans-serif; color: var(--ink); }
  .abs { position: absolute; }

  /* Top bar */
  .topbar { left: 0; top: 0; width: 1200px; height: 41px; background: var(--teal); color: var(--white); font-family: "Arimo", sans-serif; font-size: 12px; }
  .topbar .phone { position: absolute; left: 170px; top: 13px; display: flex; align-items: center; gap: 9px; }
  .topbar .account { position: absolute; right: 174px; top: 15px; letter-spacing: .3px; }

  /* Header */
  .header { left: 0; top: 41px; width: 1200px; height: 149px;
    background: linear-gradient(180deg, var(--wood-light), var(--wood-dark)); }
  .brand { position: absolute; left: 0; right: 0; top: 54px; display: flex; justify-content: center; align-items: center; gap: 12px; }
  .brand .dot { width: 40px; height: 40px; border-radius: 50%; background: var(--brown); }
  .brand .name { font-size: 26px; font-weight: 600; color: var(--white); }

  /* Nav */
  .nav { left: 0; top: 190px; width: 1200px; height: 49px; background: linear-gradient(#fdfdfd, #e4e4e4); border-top: 1px solid #cfcfcf; border-bottom: 1px solid #cfcfcf; }
  .nav ul { list-style: none; position: absolute; left: 170px; top: 0; display: flex; height: 47px; }
  .nav li { height: 47px; line-height: 47px; text-align: center; font-size: 16px; color: #222; border-right: 1px solid #cfcfcf; }
  .nav li.active { background: var(--brown); color: var(--white); }

  /* Hero */
  .hero { left: 0; top: 239px; width: 1200px; height: 582px;
    background:
      radial-gradient(ellipse 260px 330px at 920px 360px, rgba(250,250,248,.85), rgba(250,250,248,0)),
      linear-gradient(180deg, #e2ddd2 0%, #c9bfae 38%, #a29a8e 62%, #7c766f 100%); }
  .hero-caption { position: absolute; left: 170px; top: 185px; width: 475px; height: 171px; background: rgba(40,40,40,.82); color: var(--white); font-size: 29px; line-height: 49px; padding: 12px 0 0 40px; white-space: nowrap; }
  .dots { position: absolute; left: 545px; top: 559px; display: flex; gap: 8px; }
  .dots span { width: 15px; height: 15px; border-radius: 50%; background: var(--white); }
  .dots span.on { background: #3a2a1a; }

  /* Special offer */
  .offer { left: 0; top: 821px; width: 1200px; height: 191px; background: linear-gradient(#ffffff, #dedede); border-top: 1px solid #cfcfcf; }
  .ribbon { position: absolute; left: 185px; top: 0; width: 94px; }
  .ribbon .label { position: absolute; left: 0; top: 36px; width: 94px; text-align: center; font-family: "Dancing Script", cursive; font-size: 19px; line-height: 22px; color: var(--white); }
  .offer h2 { position: absolute; left: 325px; top: 24px; font-weight: 400; font-size: 26px; color: var(--teal); }
  .offer p { position: absolute; left: 324px; top: 64px; width: 540px; font-family: "Arimo", sans-serif; font-size: 14.5px; line-height: 21px; text-align: justify; text-align-last: justify; color: #444; }
  .btn { position: absolute; left: 910px; top: 75px; width: 117px; height: 40px; background: var(--brown-btn); color: var(--white); border-radius: 3px; font-size: 15px; line-height: 40px; text-align: center; box-shadow: 0 2px 2px rgba(0,0,0,.3); }

  /* Features */
  .feature { top: 1057px; width: 300px; text-align: center; }
  .feature .circle { width: 154px; height: 154px; border-radius: 50%; background: var(--teal); margin: 0 auto; display: flex; align-items: center; justify-content: center; }
  .feature h3 { margin-top: 30px; font-size: 19px; font-weight: 600; letter-spacing: .5px; color: #222; }
  .feature p { margin-top: 12px; font-family: "Arimo", sans-serif; font-size: 12.5px; line-height: 22px; color: var(--grey-text); }

  /* Plans */
  .plans { left: 0; top: 1372px; width: 1200px; height: 343px; background: var(--cream); border-top: 2px solid var(--line); border-bottom: 2px solid var(--line); }
  .plan { top: 31px; width: 279px; }
  .plan .photo { width: 279px; height: 176px; }
  .plan h4 { margin-top: 10px; font-size: 19px; font-weight: 400; color: var(--teal); }
  .plan p { margin-top: 2px; font-family: "Arimo", sans-serif; font-size: 11.3px; line-height: 21px; color: var(--grey-text); white-space: nowrap; }
  .arrow { top: 69px; }

  /* Why */
  .why-mark { left: 167px; top: 1760px; width: 240px; height: 150px; display: flex; align-items: center; gap: 10px; }
  .why-mark .dot { width: 40px; height: 40px; border-radius: 50%; background: var(--brown); flex: none; }
  .why-mark .name { font-size: 22px; font-weight: 600; color: var(--brown); line-height: 28px; }
  .why h2 { position: absolute; left: 438px; top: 1775px; font-size: 26px; font-weight: 600; color: var(--teal); white-space: nowrap; }
  .why p { position: absolute; left: 438px; top: 1829px; width: 600px; font-size: 12.3px; line-height: 22px; color: #555; }

  /* Testimonial */
  .testimonial { left: 0; top: 1970px; width: 1200px; height: 177px; background: linear-gradient(#ffffff, #e2e2e2); border-top: 2px solid var(--line); }
  .avatar { position: absolute; left: 170px; top: 19px; width: 131px; height: 131px; border-radius: 50%; background: linear-gradient(180deg, #f4f4f2 0%, #e8d6c8 45%, #f2f2f2 80%); border: 2px solid #ddd; }
  .quote { position: absolute; font-family: Georgia, serif; font-size: 42px; font-weight: 700; color: #3a2a1a; line-height: 1; }
  .testimonial blockquote { position: absolute; left: 364px; top: 45px; width: 640px; font-family: "Arimo", sans-serif; font-size: 13px; line-height: 25px; color: #333; }

  /* Footer */
  .footer { left: 0; top: 2147px; width: 1200px; height: 167px; background: var(--teal); color: var(--white); font-family: "Arimo", sans-serif; }
  .footer .links { position: absolute; left: 0; right: 0; top: 25px; text-align: center; font-size: 11.5px; }
  .footer .copy { position: absolute; left: 174px; top: 92px; font-size: 10.5px; }
  .social { position: absolute; left: 480px; top: 77px; display: flex; gap: 6px; }
  .social span { width: 34px; height: 34px; border-radius: 50%; background: #e9ecea; }
  .newsletter { position: absolute; left: 816px; top: 83px; width: 207px; height: 26px; background: var(--white); color: #777; font-size: 10.5px; line-height: 26px; padding-left: 8px; }
  .newsletter svg { position: absolute; right: 6px; top: 4px; }
</style>
</head>
<body>

<div class="abs topbar">
  <div class="phone">
    <svg width="12" height="12" viewBox="0 0 24 24"><path fill="#fff" d="M6.6 10.8a15 15 0 0 0 6.6 6.6l2.2-2.2a1 1 0 0 1 1-.25 11.4 11.4 0 0 0 3.6.57 1 1 0 0 1 1 1V20a1 1 0 0 1-1 1A17 17 0 0 1 3 4a1 1 0 0 1 1-1h3.5a1 1 0 0 1 1 1c0 1.25.2 2.45.57 3.6a1 1 0 0 1-.25 1z"/></svg>
    <span>Call : 888-555-0142</span>
  </div>
  <div class="account">SIGN IN &nbsp;|&nbsp; JOIN NOW</div>
</div>

<header class="abs header" role="img" aria-label="Warm wood-grain header background">
  <div class="brand"><span class="dot"></span><span class="name">Harvest Table Menus</span></div>
</header>

<nav class="abs nav">
  <ul>
    <li class="active" style="width:74px">HOME</li>
    <li style="width:105px">MENU</li>
    <li style="width:125px">ABOUT US</li>
    <li style="width:143px">MEAL PLANS</li>
    <li style="width:111px">GALLERY</li>
    <li style="width:159px">ONLINE ORDER</li>
    <li style="width:119px;border-right:none">CONTACT</li>
  </ul>
</nav>

<section class="abs hero" role="img" aria-label="Photo of chefs in white uniforms standing in a steel restaurant kitchen">
  <div class="hero-caption">
    65% HEALTHY FATS Per Weak<br>25% LEAN PRoTEIN per Weak<br>10% GOOD CARBS Per Weak
  </div>
  <div class="dots"><span></span><span></span><span class="on"></span><span></span><span></span></div>
</section>

<section class="abs offer">
  <div class="ribbon">
    <svg width="94" height="142" viewBox="0 0 94 142"><polygon points="0,0 94,0 94,142 47,128 0,142" fill="#3a3a3a"/><line x1="22" y1="100" x2="72" y2="100" stroke="#777" stroke-width="1"/></svg>
    <div class="label">Special<br>Offer!</div>
  </div>
  <h2>Special Offer Of The Month</h2>
  <p>We provide membership based program that delivers weekly meal programs (7 days worth of recipes plus shopping lists) carefully crafted by an expert team of meal planners. All recipes are created to comply with the following</p>
  <div class="btn">READ MORE</div>
</section>

<div class="abs feature" style="left:152px">
  <div class="circle">
    <svg width="70" height="76" viewBox="0 0 70 76" fill="none" stroke="#fff" stroke-width="3">
      <path d="M28 4c-4 5 4 8 0 14M36 2c-4 5 4 8 0 14M44 4c-4 5 4 8 0 14"/>
      <rect x="8" y="26" width="54" height="4" fill="#fff"/>
      <path d="M12 32h46v20a8 8 0 0 1-8 8H20a8 8 0 0 1-8-8z" fill="#fff"/>
      <path d="M4 36h8M58 36h8"/>
      <path d="M14 70h42M20 66v8M35 66v8M50 66v8"/>
    </svg>
  </div>
  <h3>MEAL PLANS</h3>
  <p>We provide membership based program<br>that delivers weekly meal programs</p>
</div>
<div class="abs feature" style="left:445px">
  <div class="circle">
    <svg width="80" height="80" viewBox="0 0 80 80" fill="#fff">
      <path d="M14 10 70 66l-6 6L8 16z"/>
      <ellipse cx="58" cy="20" rx="11" ry="14" transform="rotate(45 58 20)"/>
      <path d="M50 28 12 66l4 4 38-38z"/>
    </svg>
  </div>
  <h3>QUICK START GUIDE</h3>
  <p>We provide membership based program<br>that delivers weekly meal programs</p>
</div>
<div class="abs feature" style="left:740px">
  <div class="circle">
    <svg width="60" height="80" viewBox="0 0 60 80" fill="#fff">
      <path d="M16 28a10 10 0 0 1 2-18 12 12 0 0 1 24 0 10 10 0 0 1 2 18z"/>
      <rect x="18" y="30" width="24" height="5"/>
      <path d="M4 78c0-18 10-28 26-28s26 10 26 28z"/>
    </svg>
  </div>
  <h3>OUR MEMBERSHIP</h3>
  <p>We provide membership based program<br>that delivers weekly meal programs</p>
</div>

<section class="abs plans">
  <svg class="abs arrow" style="left:96px" width="28" height="90" viewBox="0 0 28 90"><polyline points="26,2 2,45 26,88" fill="none" stroke="#555" stroke-width="1.5"/></svg>
  <svg class="abs arrow" style="left:1072px" width="28" height="90" viewBox="0 0 28 90"><polyline points="2,2 26,45 2,88" fill="none" stroke="#555" stroke-width="1.5"/></svg>

  <div class="abs plan" style="left:168px">
    <div class="photo" role="img" aria-label="Photo of a bowl of fresh mixed vegetable salad" style="background:linear-gradient(160deg,#e9c9a0 0%,#c87a45 50%,#8a9a4a 100%)"></div>
    <h4>CLASSIC</h4>
    <p>Our vegetarian plans are simple, complete meals with<br>sides, and organized with cost estimates to keep you<br>on budget! We use seasonal ingredients, offering you a</p>
  </div>
  <div class="abs plan" style="left:460px">
    <div class="photo" role="img" aria-label="Photo of a packed lunch with cucumber and strawberries" style="background:linear-gradient(160deg,#d8b48e 0%,#c77a6a 50%,#cfc6a0 100%)"></div>
    <h4>GLUTEN FREE</h4>
    <p>Our vegetarian plans are simple, complete meals with<br>sides, and organized with cost estimates to keep you<br>on budget! We use seasonal ingredients, offering you a</p>
  </div>
  <div class="abs plan" style="left:750px">
    <div class="photo" role="img" aria-label="Photo of a spinach salad with chickpeas and diced vegetables" style="background:linear-gradient(160deg,#34502e 0%,#4f6b35 50%,#b48a4a 100%)"></div>
    <h4>VEGETARIAN</h4>
    <p>Our vegetarian plans are simple, complete meals with<br>sides, and organized with cost estimates to keep you<br>on budget! We use seasonal ingredients, offering you a</p>
  </div>
</section>

<section class="why">
  <div class="abs why-mark"><span class="dot"></span><span class="name">Harvest Table Menus</span></div>
  <h2>Why should I eat Harvest Table Menus?</h2>
  <p>We provide membership based program that delivers weekly meal programs (7 days worth of recipes plus shopping lists) carefully crafted by an expert team of meal planners. All recipes are created to comply with the following macronutrient ratio: 65% healthy fats, 25% lean protein, 10% good carbs</p>
</section>

<section class="abs testimonial">
  <div class="avatar" role="img" aria-label="Portrait photo of the head chef"></div>
  <span class="quote" style="left:328px;top:40px">&ldquo;</span>
  <blockquote>Lorem ipsum dolor sit amet, maiores ornare ac fermentum, imperdiet ut vivamus a, nam lectus at nunc. Quam euismod sem, semper ut potenti pellentesque quisque. In eget sapien sed, sit duis vestibulum ultricies, placerat morbi Lorem ipsum dolor sit amet, maiores ornare ac fermentum, imperdiet ut vivamus a, nam lectus at nunc.</blockquote>
  <span class="quote" style="left:1006px;top:104px">&rdquo;</span>
</section>

<footer class="abs footer">
  <div class="links">Terms of Service | Returns | Policy Privacy | Event | Contact | Blog | Sitemap</div>
  <div class="copy">Copy Right © 2014. All rights reserved.</div>
  <div class="social" aria-label="Social links"><span></span><span></span><span></span><span></span><span></span><span></span></div>
  <div class="newsletter">News Letter
    <svg width="26" height="18" viewBox="0 0 26 18"><rect x="1" y="1" width="24" height="16" fill="#fff" stroke="#333" stroke-width="2"/><polyline points="1,1 13,10 25,1" fill="none" stroke="#333" stroke-width="2"/></svg>
  </div>
</footer>

</body>
</html>
```